Vorniclean.net

This is a postcard for a Dry Cleaning Business .Please find attached the info I want to put in. Please use the pictures I attached . Keep the pictures on top
You can change the lay out of the bottom part as you see fit.
Keep the blue on the background for the bottom

Make the coupon 10% off to look better

This is the final layout .

Please make it look good I I will buy your design .

Target Market(s)

Up scale neighborhood

Industry/Entity Type

Business

Requirements
Must have
• Vornclean.net ( the company name ) should be in blue

```html
<!DOCTYPE html>
<html lang="en">
<head>
<meta charset="utf-8">
<title>Vorniclean.net Postcard</title>
<link rel="stylesheet" href="https://fonts.googleapis.com/css2?family=Oswald:wght@400;500;600;700&family=Open+Sans:wght@400;600;700;800&display=swap">
<style>
  :root {
    --navy: #16356f;
    --navy-deep: #0d2552;
    --blue: #1f4a94;
    --red: #d4202a;
    --red-deep: #a9141c;
    --white: #ffffff;
    --ink: #1b1b1b;
    --page: #eceef1;
    --rule: #3a3a3a;
  }
  * { margin: 0; padding: 0; box-sizing: border-box; }
  html, body { width: 800px; height: 1200px; overflow: hidden; }
  body { background: var(--page); position: relative; font-family: "Open Sans", sans-serif; }

  .postcard { position: absolute; left: 50px; width: 700px; height: 544px; overflow: hidden; box-shadow: 0 3px 10px rgba(0,0,0,.18); }
  .postcard--front { top: 60px; background: var(--white); }
  .postcard--back { top: 630px; background: var(--white); }

  .photo { position: absolute; top: 0; height: 300px; }
  .photo--one { left: 0; width: 148px; background: linear-gradient(160deg, #b9b3aa, #6f6a66 60%, #3d3b3c); }
  .photo--two { left: 150px; width: 182px; background: linear-gradient(170deg, #c8c2b6, #8b8479 55%, #56514d); }
  .photo--three { left: 336px; width: 164px; background: linear-gradient(170deg, #9a8f86, #5d6170 55%, #2e3340); }
  .photo--four { left: 503px; width: 197px; background: linear-gradient(170deg, #d3ccbf, #9a9388 55%, #6b665f); }

  .front-shapes { position: absolute; inset: 0; }

  .coupon { position: absolute; left: 25px; top: 140px; width: 234px; height: 234px; display: flex; flex-direction: column; align-items: center; justify-content: center; text-align: center; font-family: "Oswald", sans-serif; line-height: 1; }
  .coupon__lead { color: var(--white); font-size: 23px; font-weight: 500; }
  .coupon__small { color: var(--ink); font-size: 16px; font-weight: 400; margin-top: 4px; }
  .coupon__amount { color: var(--white); font-size: 50px; font-weight: 600; margin-top: 4px; }
  .coupon__for { color: var(--ink); font-size: 19px; font-weight: 400; margin-top: 6px; }
  .coupon__term { color: var(--white); font-size: 21px; font-weight: 500; margin-top: 4px; }

  .stop-sign { position: absolute; left: 241px; top: 98px; width: 166px; height: 166px; }

  .service-info { position: absolute; left: 28px; top: 0; width: 260px; height: 544px; font-family: "Oswald", sans-serif; color: var(--white); line-height: 1; }
  .service-info__hours { position: absolute; top: 412px; left: 0; font-size: 14px; font-weight: 400; letter-spacing: .2px; white-space: nowrap; }
  .service-info__time { position: absolute; top: 432px; left: 0; display: flex; align-items: center; gap: 10px; font-size: 22px; font-weight: 500; white-space: nowrap; }
  .service-info__bar { display: block; width: 110px; height: 19px; background: var(--red); }
  .service-info__call { position: absolute; top: 462px; left: 0; font-size: 25px; font-weight: 500; white-space: nowrap; }
  .service-info__call-label { color: var(--red); font-size: 21px; margin-right: 6px; }

  .headline { position: absolute; left: 314px; top: 0; width: 362px; height: 544px; text-align: center; }
  .headline__main { position: absolute; top: 344px; left: 0; width: 100%; font-family: "Oswald", sans-serif; font-size: 38px; font-weight: 500; color: var(--white); line-height: 1; white-space: nowrap; }
  .headline__rule { position: absolute; top: 395px; left: 5px; width: 352px; height: 4px; background: var(--red); }
  .headline__sub { position: absolute; top: 402px; left: 0; width: 100%; font-size: 17px; font-weight: 400; color: var(--white); letter-spacing: .3px; line-height: 1.2; white-space: nowrap; }
  .headline__cta { position: absolute; top: 423px; left: 0; width: 100%; font-family: "Oswald", sans-serif; font-size: 44px; font-weight: 500; color: var(--red); line-height: 1; white-space: nowrap; }

  .website { position: absolute; left: 330px; width: 340px; top: 496px; text-align: center; color: var(--navy); font-weight: 800; font-size: 15px; letter-spacing: 3px; line-height: 1.2; }

  .stamp-box { position: absolute; left: 580px; top: 53px; width: 95px; height: 114px; border: 1.5px solid var(--rule); }
  .address-line { position: absolute; left: 357px; width: 317px; height: 2px; background: var(--rule); }
  .address-line--one { top: 348px; }
  .address-line--two { top: 381px; }
  .address-line--three { top: 414px; }
</style>
</head>
<body>

<section class="postcard postcard--front">
  <div class="photo photo--one" role="img" aria-label="Customer carrying dry-cleaned garments in plastic bags"></div>
  <div class="photo photo--two" role="img" aria-label="Woman walking with dry-cleaned clothes by a parked car"></div>
  <div class="photo photo--three" role="img" aria-label="Man in a hooded jacket carrying garment bags"></div>
  <div class="photo photo--four" role="img" aria-label="Woman walking down the street holding dry-cleaned clothes"></div>

  <svg class="front-shapes" width="700" height="544" viewBox="0 0 700 544" aria-hidden="true">
    <defs>
      <linearGradient id="panelBlue" x1="0" y1="0" x2="0" y2="1">
        <stop offset="0" stop-color="#1f4a94"/>
        <stop offset="1" stop-color="#0d2552"/>
      </linearGradient>
      <linearGradient id="bandRed" x1="0" y1="0" x2="1" y2="0">
        <stop offset="0" stop-color="#a9141c"/>
        <stop offset=".5" stop-color="#d4202a"/>
        <stop offset="1" stop-color="#a9141c"/>
      </linearGradient>
      <radialGradient id="couponRed" cx=".5" cy=".45" r=".6">
        <stop offset="0" stop-color="#e0262f"/>
        <stop offset="1" stop-color="#b2161e"/>
      </radialGradient>
    </defs>
    <path d="M0,238 C180,300 420,330 700,250 L700,300 C440,352 200,330 0,262 Z" fill="#d4202a"/>
    <path d="M0,250 C190,312 430,344 700,272 L700,318 C440,362 200,340 0,272 Z" fill="#ffffff"/>
    <path d="M0,262 C200,330 440,370 700,320 L700,544 L0,544 Z" fill="url(#panelBlue)"/>
    <path d="M0,500 L300,500 C340,500 352,478 392,478 L700,478 L700,544 L0,544 Z" fill="#ffffff"/>
    <path d="M0,506 L302,506 C342,506 356,484 396,484 L700,484 L700,544 L0,544 Z" fill="url(#bandRed)"/>
    <circle cx="142" cy="257" r="117" fill="#ffffff"/>
    <circle cx="142" cy="257" r="109" fill="url(#couponRed)"/>
  </svg>

  <svg class="stop-sign" viewBox="0 0 166 166" aria-hidden="true">
    <polygon points="49,2 117,2 164,49 164,117 117,164 49,164 2,117 2,49" fill="#ffffff"/>
    <polygon points="52,9 114,9 157,52 157,114 114,157 52,157 9,114 9,52" fill="#d4202a"/>
    <text x="83" y="102" text-anchor="middle" font-family="Oswald, sans-serif" font-weight="700" font-size="52" fill="#ffffff">STOP</text>
  </svg>

  <div class="coupon">
    <span class="coupon__lead">SIGN UP</span>
    <span class="coupon__small">THIS WEEK TO RECEIVE</span>
    <span class="coupon__amount">10% OFF</span>
    <span class="coupon__for">FOR THE</span>
    <span class="coupon__term">NEXT 3 MONTH</span>
  </div>

  <div class="service-info">
    <p class="service-info__hours">LATE HOURS FREE PICKUP &amp; DELIVERY</p>
    <p class="service-info__time">UPTO 10 PM <span class="service-info__bar"></span></p>
    <p class="service-info__call"><span class="service-info__call-label">CALL</span>650 555 0148</p>
  </div>

  <div class="headline">
    <h1 class="headline__main">STOP DRIVING AROUND</h1>
    <span class="headline__rule"></span>
    <p class="headline__sub">YOUR DRY-CLEANING SERVICE IS</p>
    <p class="headline__cta">ONE CLICK AWAY</p>
  </div>

  <p class="website">www.vorniclean.net</p>
</section>

<section class="postcard postcard--back">
  <div class="stamp-box"></div>
  <span class="address-line address-line--one"></span>
  <span class="address-line address-line--two"></span>
  <span class="address-line address-line--three"></span>
</section>

</body>
</html>
```